Brookvale Auto Hire- car rental & accident claim management

We need a web design for a company based in Sydney called "Brookvale Auto Hire". We are a rental car company, who also specialise in not at fault accident claim management. when a client is not at fault in an accident, if they can provided us with the At Fault Parties (AFP) insurance details and claim number we can provide them with a rental car whilst their car is repaired (or if it is a total loss) and claim the costs of the rental car from the AFP's insurance company.
-rental vehicles
-accident repalcement vehicles
-third party recovery
-independent assessments
Our fleet comprises of small to large vehicles, including SUV's 4WD's, Prestige and commercial.
Our companies colour is bright green, so we would like it to be in keeping with that. we have two logo's. we would prefer the web page to use a bright/lime green (brighther than our logo).
we would ask that our design communicates quality, commitment to customer service and make our clients feel safe.
our competitors include: Meridian Recoveries and TKL if you would like to peruse these companies to get an idea of our industry. (tkl.example.au and meridianrecoveries.example.au)
Requirements
Must have
- telephone number to come. we are in the middle of chaniging so please leave space for the new phone number (once allocated to us) thank you

```html
<!DOCTYPE html>
<html lang="en">
<head>
<meta charset="utf-8">
<title>Brookvale Auto Hire</title>
<link href="https://fonts.googleapis.com/css2?family=Open+Sans:wght@400;600;700&display=swap" rel="stylesheet">
<style>
:root{
  --page-green:#3b8f23;
  --page-green-dark:#2f7a1b;
  --lime:#5fd12a;
  --frame:#57d62a;
  --heading-green:#2f8a12;
  --text:#222;
  --tab:#2b2b2b;
  --orange:#f06a10;
  --box-line:#3a9a1a;
  --field:#3a9a2a;
  --field-line:#5cc23a;
  --footer-text:#1a3d0c;
}
*{box-sizing:border-box;margin:0;padding:0}
html,body{width:1183px;height:1200px;overflow:hidden}
body{background:radial-gradient(ellipse at 50% 40%,var(--page-green) 0%,var(--page-green-dark) 100%);font-family:"Open Sans",sans-serif;color:var(--text);position:relative}
.sheet{position:absolute;left:186px;top:34px;width:811px;height:965px;background:#fff;border:7px solid var(--frame)}
.brand{position:absolute;left:207px;top:90px;display:flex;align-items:center;gap:8px;font-size:22px;font-weight:700;color:var(--heading-green)}
.brand-dot{width:18px;height:18px;border-radius:50%;background:var(--heading-green)}
.phone{position:absolute;right:213px;top:56px;display:flex;align-items:center;gap:10px;font-size:19px;color:#111}
.nav{position:absolute;left:363px;top:142px;display:flex;gap:4px}
.nav a{display:block;height:26px;padding:0;text-align:center;line-height:27px;font-size:12px;color:#fff;text-decoration:none;background:linear-gradient(#4a4a4a,var(--tab));border-radius:5px 5px 0 0;border:1px solid #111;border-bottom:none;white-space:nowrap}
.hero{position:absolute;left:177px;top:163px;width:829px;height:254px;background:var(--lime);border-radius:6px;overflow:hidden}
.hero-photo{position:absolute;right:0;top:6px;width:580px;height:242px;background:linear-gradient(90deg,var(--lime) 0%,#7cb75a 25%,#6f7a6a 55%,#5a6258 80%,var(--lime) 100%)}
.hero-copy{position:absolute;left:25px;top:28px;width:400px}
.hero-copy h1{font-size:19px;font-weight:400;line-height:26px;color:#111}
.hero-list{list-style:none;margin-top:13px}
.hero-list li{font-size:12px;line-height:21.7px;padding-left:30px;position:relative;color:#1b2d10}
.hero-list li::before{content:"";position:absolute;left:12px;top:7px;width:8px;height:8px;border-radius:50%;background:#ffc400;border:1px solid #c78a00}
.claim-btn{position:absolute;left:31px;top:191px;width:155px;height:36px;border-radius:7px;background:linear-gradient(#ff8a2a,var(--orange));border:3px solid #ff9e55;color:#fff;font-weight:700;font-size:15px;text-align:center;line-height:30px}
.welcome{position:absolute;left:217px;top:432px;width:740px}
.welcome h2{font-size:18px;font-weight:400;color:var(--heading-green)}
.welcome p{margin-top:10px;font-size:10.6px;line-height:15.3px}
.read-more{position:absolute;right:226px;top:533px;font-size:11px;color:var(--heading-green);text-decoration:underline}
.read-more::after{content:"";display:inline-block;margin-left:6px;border:4px solid transparent;border-left:5px solid #333;border-right:none}
.card{position:absolute;top:565px;width:238px;height:212px;background:linear-gradient(#fff,#e6e6e6);border:1px solid #cfcfcf;border-top:2px solid var(--box-line);border-bottom:2px solid var(--box-line)}
.card h3{position:absolute;left:12px;top:12px;font-size:13px;font-weight:700;color:var(--heading-green);display:flex;align-items:center;gap:8px}
.card h3 span{color:#777}
.card-rule{position:absolute;left:10px;right:10px;top:42px;height:1px;background:linear-gradient(90deg,#ddd,#fff)}
.ticks{position:absolute;left:16px;top:68px;list-style:none}
.ticks li{font-size:11px;line-height:21.7px;display:flex;align-items:center;gap:10px}
.card-text{position:absolute;left:16px;top:66px;width:210px;font-size:11px;line-height:17px}
.quote{position:absolute;left:16px;top:60px;width:205px;height:100px;background:#fff;border:1px solid #ddd;border-radius:3px;padding:8px 10px;font-size:11px;line-height:17px}
.quote::after{content:"";position:absolute;right:18px;bottom:-9px;border:8px solid transparent;border-top:8px solid #fff;border-bottom:none}
.author{position:absolute;right:18px;top:170px;font-size:11px;font-weight:700;color:#333}
.card-btn{position:absolute;right:18px;bottom:-2px;width:84px;height:22px;background:linear-gradient(#3aa01a,#237a0c);color:#fff;font-size:11.5px;text-align:center;line-height:22px;border-radius:4px 4px 0 0}
.partners-title{position:absolute;left:0;width:1183px;top:800px;text-align:center;font-size:16px;font-weight:700;color:var(--heading-green)}
.carousel{position:absolute;left:220px;top:832px;width:742px;height:115px;background:#fff;border:5px solid #eee;border-radius:6px;box-shadow:0 2px 3px #ddd}
.arrow{position:absolute;top:39px;width:27px;height:27px}
.partner-badge{position:absolute;top:22px;width:62px;height:62px;border-radius:50%;background:#d8d8d8;border:3px solid #c2c2c2}
.social{position:absolute;left:187px;top:1022px;display:flex;gap:4px}
.social span{width:25px;height:25px;border-radius:3px;background:#9fd48a;border:1px solid #2a6a16}
.footer-links{position:absolute;left:188px;top:1060px;width:390px;font-size:11px;line-height:17px;color:var(--footer-text)}
.copyright{position:absolute;left:188px;top:1167px;font-size:10.5px;color:#6fd044}
.quick{position:absolute;left:650px;top:1008px;width:349px}
.quick h4{font-size:16px;font-weight:700;color:#7bee4a}
.field{position:absolute;height:25px;background:var(--field);border:1px solid var(--field-line);border-radius:4px;color:#9ef07a;font-size:10.5px;padding:6px 11px}
.submit{position:absolute;left:266px;top:160px;width:83px;height:23px;background:var(--lime);border:1px solid #9cf07a;border-radius:4px;text-align:center;font-size:12px;line-height:21px;color:#143a08}
</style>
</head>
<body>
<div class="sheet"></div>

<div class="brand"><span class="brand-dot"></span>Brookvale Auto Hire</div>

<div class="phone">
  <svg width="26" height="22" viewBox="0 0 26 22"><path d="M3 7c0-3 4-5 10-5s10 2 10 5v2h-5V6H8v3H3z" fill="#666"/><rect x="5" y="10" width="16" height="11" rx="2" fill="#888"/><rect x="9" y="12" width="8" height="6" fill="#bbb"/></svg>
  <span>02 5550 0000</span>
</div>

<nav class="nav">
  <a style="width:68px">Home</a><a style="width:79px">About Us</a><a style="width:75px">Services</a><a style="width:106px">Our Partners</a><a style="width:66px">FAQs</a><a style="width:100px">Claim Form</a><a style="width:93px">Contact Us</a>
</nav>

<section class="hero">
  <div class="hero-photo" role="img" aria-label="Smiling driver leaning out of a car window"></div>
  <div class="hero-copy">
    <h1>Lorem ipsum dolor sit amet consectetur adipiscing elit</h1>
    <ul class="hero-list">
      <li>Rental Vehicles</li>
      <li>Accident Repalcement Vehicles</li>
      <li>Third Party Recovery</li>
      <li>Independent Assessments</li>
    </ul>
  </div>
  <div class="claim-btn">CLAIM NOW</div>
</section>

<section class="welcome">
  <h2>Welcome to Brookvale Auto Hire</h2>
  <p>Lorem ipsum dolor sit amet, consectetur adipiscing elit. Nam scelerisque dapibus volutpat. Cum sociis natoque penatibus et magnis dis parturient montes, nascetur ridiculus mus. Pellentesque congue eleifend mi nec molestie. Sed vitae eleifend quam. Maecenas non risus sapien. Vestibulum sit amet urna augue. Fusce iaculis imperdiet purus et porta. Praesent imperdiet, eros eget consectetur bibendum, orci tortor egestas urna, a scelerisque quam sem blandit sapien.</p>
</section>
<a class="read-more">Read more</a>

<article class="card" style="left:218px">
  <h3><svg width="24" height="24" viewBox="0 0 24 24"><circle cx="9" cy="9" r="6" fill="none" stroke="#8aa" stroke-width="3"/><circle cx="17" cy="17" r="4" fill="none" stroke="#8aa" stroke-width="2.5"/></svg><span>OUR</span> SERVICES</h3>
  <div class="card-rule"></div>
  <ul class="ticks">
    <li><svg width="13" height="11"><path d="M1 6l4 4 7-9" fill="none" stroke="#3aa01a" stroke-width="3"/></svg>Rental Vehicles</li>
    <li><svg width="13" height="11"><path d="M1 6l4 4 7-9" fill="none" stroke="#3aa01a" stroke-width="3"/></svg>Accident Repalcement Vehicles</li>
    <li><svg width="13" height="11"><path d="M1 6l4 4 7-9" fill="none" stroke="#3aa01a" stroke-width="3"/></svg>Third Party Recovery</li>
    <li><svg width="13" height="11"><path d="M1 6l4 4 7-9" fill="none" stroke="#3aa01a" stroke-width="3"/></svg>Independent Assessments</li>
  </ul>
  <div class="card-btn">Read More</div>
</article>

<article class="card" style="left:472px">
  <h3><svg width="28" height="24" viewBox="0 0 28 24"><ellipse cx="14" cy="13" rx="12" ry="8" fill="#1b5fb0" transform="rotate(30 14 13)"/></svg><span>ONLINE</span> TRACKING</h3>
  <div class="card-rule"></div>
  <p class="card-text">Lorem ipsum dolor sit amet, consecte-tur adipiscing elit. Nam scelerisque dapibus volutpat. Pellentesque congue eleifend mi nec molestie. Sed vitae eleifend quam. Maecenas non risus sapien. Vestibulum sit amet urna augue non risus sapien.</p>
  <div class="card-btn">Track Now</div>
</article>

<article class="card" style="left:726px">
  <h3><svg width="24" height="26" viewBox="0 0 24 26"><path d="M3 1h12l5 5v18H3z" fill="#fff" stroke="#999"/><circle cx="18" cy="21" r="4" fill="#f5b800"/></svg>TESTIMONIALS</h3>
  <div class="card-rule"></div>
  <div class="quote">Lorem ipsum dolor sit amet, con sectetur adipiscing elit. Nam scele risque dapibus volutpat. Pelle min tesque congue eleifend mi nec molestie.</div>
  <div class="author">Daniel Marsh</div>
  <div class="card-btn">Read More</div>
</article>

<h2 class="partners-title">Our Partners</h2>
<div class="carousel">
  <svg class="arrow" style="left:12px" viewBox="0 0 27 27"><circle cx="13.5" cy="13.5" r="12.5" fill="#3aa01a" stroke="#fff" stroke-width="2"/><path d="M20 13.5H8M13 8l-5.5 5.5L13 19" fill="none" stroke="#fff" stroke-width="3"/></svg>
  <div class="partner-badge" style="left:65px;border-radius:12px"></div>
  <div class="partner-badge" style="left:153px;background:#2a2a2a;border-color:#111"></div>
  <div class="partner-badge" style="left:246px;width:70px;border-radius:14px"></div>
  <div class="partner-badge" style="left:351px"></div>
  <div class="partner-badge" style="left:448px;width:86px;border-radius:30px"></div>
  <div class="partner-badge" style="left:566px;width:100px;height:40px;top:33px"></div>
  <svg class="arrow" style="left:692px" viewBox="0 0 27 27"><circle cx="13.5" cy="13.5" r="12.5" fill="#3aa01a" stroke="#fff" stroke-width="2"/><path d="M7 13.5h12M14 8l5.5 5.5L14 19" fill="none" stroke="#fff" stroke-width="3"/></svg>
</div>

<div class="social" aria-label="Social links"><span></span><span></span><span></span><span></span></div>
<nav class="footer-links">Home | About Us | Our Services | Our Partners | FAQs | Claim Form | Contact Us | Terms and Conditions</nav>
<p class="copyright">Copyright © 2012 Brookvale Auto Hire. All rights reserved.</p>

<form class="quick">
  <h4>Quick Contact</h4>
  <div class="field" style="left:1px;top:33px;width:170px">Name</div>
  <div class="field" style="left:178px;top:33px;width:171px">Email</div>
  <div class="field" style="left:1px;top:66px;width:348px;height:84px">Message</div>
  <div class="submit">Submit</div>
</form>
</body>
</html>
```